Church needs a street sign design

We're a small church located in Silicon Valley, California. Our website is https://www.hpkwendell.org/ and our address is 1847 Thornby Ave, San Jose, California, 95871. You can look up our location on Google Maps to see the sign from Street View. I have uploaded an image of the street sign as well. The marquee, the top section of the sign, and the separating line between them both will be removed. We're seeking a design for a new backlit acrylic insert that will go on the front of the light box and the back of the lightbox. The acrylic sign will fill the entire external frame. In the future, we may build a decorative wood frame around the structural legs, as visualized in one of the uploaded files. The church's brand colors are: #003366 (dark blue), #ff6600 (vibrant orange), #228b22 (forest green). I have also uploaded the church's logo assets. Our primary font is Montserrat and the secondary is Poppins. You can deviate from these colors/fonts if the sign is still coherent with the rest of our branding. Our branding values are mission, truth, passion, and community (please do not put those words on the sign! They are just intended to guide the look of the design). The sign dimensions are 96" by 47.5". Keep in mind that the sign will be backlit on a busy street side. It will also be positioned next to an old-looking church building. We do NOT want a sign that looks traditional, old, or antiquated. Instead, we want a modern-looking sign that pairs well with our old building while helping it look more modern too. We would also like the web address clearly visible on the sign: hpkwendell.org. If you have any questions, just let me know!

```html
<!DOCTYPE html>
<html lang="en">
<head>
<meta charset="utf-8">
<title>Hillpoint Kingdom Church – Street Sign Insert</title>
<link rel="stylesheet" href="https://fonts.googleapis.com/css2?family=Montserrat:wght@400;500;600&display=swap">
<style>
  :root {
    --page: #ffffff;
    --blue-core: #04498c;
    --blue-mid: #033f7c;
    --blue-edge: #003366;
    --ink: #ffffff;
    --glow: rgba(255, 255, 255, 0.55);
  }
  * { box-sizing: border-box; margin: 0; padding: 0; }
  html, body {
    width: 1200px;
    height: 1164px;
    overflow: hidden;
    background: var(--page);
  }
  body { position: relative; font-family: "Montserrat", sans-serif; color: var(--ink); }

  .sign-insert {
    position: absolute;
    left: 0;
    top: 285px;
    width: 1200px;
    height: 593px;
    background: radial-gradient(ellipse 70% 75% at 50% 40%, var(--blue-core) 0%, var(--blue-mid) 55%, var(--blue-edge) 100%);
    overflow: hidden;
  }

  .brand {
    position: absolute;
    left: 60px;
    top: 84px;
    display: flex;
    align-items: center;
    gap: 22px;
  }
  .brand-mark {
    width: 76px;
    height: 76px;
    border: 6px solid var(--ink);
  }
  .brand-name {
    font-weight: 600;
    line-height: 1;
    color: var(--ink);
  }
  .brand-name .primary { display: block; font-size: 50px; letter-spacing: -0.5px; }
  .brand-name .secondary { display: block; font-size: 17px; margin-top: 8px; letter-spacing: 0.2px; }

  .mission {
    position: absolute;
    left: 0;
    right: 0;
    top: 206px;
    text-align: center;
    font-weight: 500;
    font-size: 76px;
    line-height: 76px;
    letter-spacing: -0.3px;
    text-shadow: 0 0 6px var(--glow), 0 0 2px var(--glow);
  }

  .web-address {
    position: absolute;
    left: 57px;
    top: 530px;
    font-size: 27px;
    font-weight: 500;
    letter-spacing: 0.3px;
  }

  .schedule {
    position: absolute;
    left: 798px;
    top: 522px;
    font-size: 18px;
    font-weight: 500;
    line-height: 21px;
    letter-spacing: 0.4px;
  }
</style>
</head>
<body>
  <main class="sign-insert">
    <div class="brand">
      <span class="brand-mark" aria-hidden="true"></span>
      <div class="brand-name">
        <span class="primary">HILLPOINT</span>
        <span class="secondary">KINGDOM CHURCH</span>
      </div>
    </div>

    <h1 class="mission">
      Making Disciples &amp;<br>
      Helping the Helpless<br>
      For the Glory of Christ
    </h1>

    <p class="web-address">www.hpkwendell.org</p>

    <p class="schedule">
      Sunday Service: 10:40 AM - 12:15 PM<br>
      Lunch Provided: 12:30 PM - 1:30 PM
    </p>
  </main>
</body>
</html>
```